Whimsical sticker needed for heavenly microwave single serve cake/treat (mug cake)

Sticker design needed for a delicious microwaveable single serve cake. The amazingly cute sticker you design will be applied to the front of a 4"x5" white single serve pouch. We will add an additional flavor sticker to define each SKU, so your design just needs to represent the concept of a fresh baked "cake"-ready in a minute. (We have brownies, muffins, pancakes, and crumb cake varieties, so don't let the design limit the assortment of flavors/varieties please.)

Looking for something whimsical and fun, that appeals to both sexes, that are having a sweet tooth attack!

Warm Crumbs by Hollis is the brand name this product will be offered under.

Sticker size needs to be 3.8" x 3.8" please.

Excited to see what you come up with! Will send small logo once we decide on a design. ;-)

Attached is an image of a similar concept for comparison.

Our logo color is PMS 239. This is a link to our products packaging palette colors. https://www.huevault.example/articles/color-palettes/vivify-a-cheerful-palette-expressing-freshness-and-positivity.

The other attachment is the background pattern design we use on other packaging.

Let's use your amazing talent, to make our fun concept really pop!
Updates

If adding cupcake illustrations, We like these: https://www.pixelbarn.example/vector/pattern-of-cartoon-cupcakes-on-white-isolated-background-cakes-as-a-vector-stock-gm1280936724-379114338 https://www.pixelbarn.example/vector/muffins-gm165632220-9555959 https://www.pixelbarn.example/vector/cartoon-muffins-set-gm513806304-87799445

Target Market(s)

Both women and men 21+ looking for a more upscale fun cannabis edibles than gummies.

Industry/Entity Type

Cannabis

Font styles to use
Serif
Other font styles liked:
• Match other packaging example if possible

Colors
e667a6
abd037
85acd3
e34197
b8a6cd
fbed22
9bcb3c

Requirements
Must have
• Clean & fresh design. See example of our bath product packaging which was uploaded as inspiration. Will provide logo shortly. Logo color is PMS 139. But not too much pink on this design, as we want it to appeal to men too.

Needs red THC warning symbol & Contains Marijuana. Keep away from Children. Font for this warning needs to be at minimum 1/16" Red symbol must be 1/2" tall.

Single Serving.

Need this sticker you are designing to be universal for all our flavors and THC strengths that we offer.
Nice to have
• Perhaps use little chef hat and mug with steam, similar to how we used graphics on the bath products - please see packaging example attached?

Directions like "Pour in a mug, add water, microwave, ENJOY!"

www.hollisorvo.example
Should not have
• No cannabis leaves or stereotypical stoner looking graphics please.

```html
<!DOCTYPE html>
<html lang="en">
<head>
<meta charset="utf-8">
<title>Hollis mug cake sticker</title>
<link rel="stylesheet" href="https://fonts.googleapis.com/css2?family=Libre+Bodoni:wght@700&family=Kaushan+Script&family=Oswald:wght@500&display=swap">
<style>
  :root {
    --magenta: #d04a9e;
    --pink-soft: #e08fc0;
    --lime: #9bcb3c;
    --lime-deep: #7fae2a;
    --lime-pale: #dfeab0;
    --warn-red: #e3242b;
    --white: #ffffff;
    --butter: #f6e827;
  }
  html, body {
    margin: 0;
    padding: 0;
    width: 1200px;
    height: 773px;
    overflow: hidden;
    background: var(--white);
  }
  .sticker-sheet { display: block; width: 1200px; height: 773px; }
  .brand-name { font-family: "Oswald", "Arial Narrow", sans-serif; font-weight: 500; font-size: 40px; letter-spacing: 8px; fill: var(--lime-deep); }
  .product-line { font-family: "Libre Bodoni", Georgia, serif; font-weight: 700; font-size: 30px; fill: var(--white); }
  .tagline { font-family: "Kaushan Script", cursive; font-size: 44px; fill: var(--white); }
  .tagline-accent { font-size: 54px; }
  .tagline-rule { fill: none; stroke: var(--white); stroke-width: 2.5; stroke-linecap: round; }
  .warning-text { font-family: "Oswald", "Arial Narrow", sans-serif; font-weight: 500; font-size: 10.5px; fill: var(--white); letter-spacing: 0.2px; }
  .warning-diamond { fill: var(--white); stroke: var(--warn-red); stroke-width: 4; }
  .warning-label { font-family: "Oswald", "Arial Narrow", sans-serif; font-weight: 500; font-size: 17px; fill: var(--warn-red); }
  .warning-mark { fill: var(--warn-red); }
  .directions { font-family: "Libre Bodoni", Georgia, serif; font-weight: 700; font-size: 16px; letter-spacing: 0.6px; word-spacing: 2px; fill: var(--white); }
  .web-address { font-family: "Libre Bodoni", Georgia, serif; font-weight: 700; font-size: 19px; letter-spacing: 0.5px; fill: var(--white); }
  .url-band { fill: var(--magenta); }
  .inner-top { fill: var(--white); }
  .inner-field { fill: var(--lime); }
</style>
</head>
<body>
<svg class="sticker-sheet" viewBox="0 0 1200 773" xmlns="http://www.w3.org/2000/svg">
  <defs>
    <linearGradient id="ring-tones" x1="0" y1="0" x2="1" y2="1">
      <stop offset="0" stop-color="#d04a9e"/>
      <stop offset="0.35" stop-color="#e08fc0"/>
      <stop offset="0.6" stop-color="#dfeab0"/>
      <stop offset="1" stop-color="#d04a9e"/>
    </linearGradient>
    <linearGradient id="kitchen-tones" x1="0" y1="0" x2="1" y2="1">
      <stop offset="0" stop-color="#e6e6ea"/>
      <stop offset="1" stop-color="#f6e827"/>
    </linearGradient>
    <clipPath id="inner-disc"><circle cx="0" cy="0" r="214"/></clipPath>
    <path id="directions-arc" d="M -196 -28 A 198 198 0 1 0 196 -28"/>
    <path id="address-arc" d="M -231 0 A 231 231 0 0 0 231 0"/>

    <g id="sticker-base">
      <circle class="pattern-ring" cx="0" cy="0" r="252" fill="url(#ring-tones)" role="img" aria-label="Quatrefoil lattice pattern in pink and lime"/>
      <path class="url-band" d="M 126.0 218.2 L 109.2 181.5 A 214 214 0 0 1 -109.2 181.5 L -126.0 218.2 A 252 252 0 0 0 126.0 218.2 Z"/>
      <circle class="inner-top" cx="0" cy="0" r="214"/>
      <rect class="inner-field" x="-214" y="-134" width="428" height="360" clip-path="url(#inner-disc)"/>
      <text class="brand-name" x="4" y="-158" text-anchor="middle">HOLLIS</text>
      <text class="product-line" x="0" y="-100" text-anchor="middle">fresh baked cake</text>
      <text class="tagline" x="4" y="-40" text-anchor="middle">ready in a <tspan class="tagline-accent" dy="-6">minute</tspan></text>
      <path class="tagline-rule" d="M 54 -34 Q 120 -44 190 -42"/>
      <rect class="kitchen-art" x="-67" y="-30" width="134" height="92" rx="18" fill="url(#kitchen-tones)" role="img" aria-label="Chef hat, whisk and steaming yellow mug"/>
      <g class="thc-warning">
        <polygon class="warning-diamond" points="0,70 37,106 0,142 -37,106"/>
        <rect class="warning-mark" x="-2" y="78" width="4" height="13" rx="1.5"/>
        <circle class="warning-mark" cx="0" cy="95" r="2.4"/>
        <text class="warning-label" x="0" y="116" text-anchor="middle">THC</text>
      </g>
      <text class="warning-text" x="0" y="154" text-anchor="middle">CONTAINS MARIJUANA.</text>
      <text class="warning-text" x="0" y="167" text-anchor="middle">KEEP AWAY FROM CHILDREN.</text>
      <text class="web-address"><textPath href="#address-arc" startOffset="50%" text-anchor="middle">hollisessentials.example</textPath></text>
    </g>
  </defs>

  <g class="sticker sticker-single" transform="translate(310 383)">
    <use href="#sticker-base"/>
    <text class="directions"><textPath href="#directions-arc" startOffset="50%" text-anchor="middle">Single Serving / Direction: Pour in a mug, add water, microwave, ENJOY!</textPath></text>
  </g>

  <g class="sticker sticker-multi" transform="translate(860 383)">
    <use href="#sticker-base"/>
    <text class="directions"><textPath href="#directions-arc" startOffset="50%" text-anchor="middle">10 Servings / Direction: Pour in a mug, add water, microwave, ENJOY!</textPath></text>
  </g>
</svg>
</body>
</html>
```